A Label for an ECO Friendly Spirit Company

Design a label which can be used for vodka and gin (London Dry Gin). It should be Square type Like the Shape File you see in the uploads. VORN means Local Eco friendly Authentic and Fair. We want a cool and slim label that calls for eco-friendly. We want to use it for our premium
Vodka and our London Dry Gin. Please use the logo and design it in Square Type.

40%vol, 700ml

Target Market(s)

spirits and events

Industry/Entity Type

SPIRITS

Colors
00AB8E
00BBA5
67D7C9
C6EFE9
E9F9F6
59FF00
82FF00
B8FF75
E3FFCB
F4FFEA

Requirements
Must have
• Logo from VORN, Squaee Shape

```html
<!DOCTYPE html>
<html lang="en">
<head>
<meta charset="utf-8">
<title>VORN Spirits Labels</title>
<link rel="stylesheet" href="https://fonts.googleapis.com/css2?family=Smokum&family=Montserrat:wght@600&family=Arimo&display=swap">
<style>
  :root {
    --paper: #ffffff;
    --ink: #ffffff;
    --gin-deep: #03120f;
    --gin-mid: #0b3a31;
    --gin-bright: #1a8f7c;
    --gin-line: #1fb59b;
    --vodka-deep: #101a05;
    --vodka-mid: #2c4510;
    --vodka-bright: #6a9e2a;
    --vodka-line: #72d63c;
  }
  html, body {
    margin: 0;
    padding: 0;
    width: 1200px;
    height: 723px;
    overflow: hidden;
    background: var(--paper);
  }
  .canvas {
    position: relative;
    width: 1200px;
    height: 723px;
  }
  .label {
    position: absolute;
    top: 107px;
    width: 528px;
    height: 528px;
  }
  .label--gin { left: 77px; }
  .label--vodka { left: 626px; }
  .brand-name {
    font-family: "Montserrat", sans-serif;
    font-weight: 600;
    fill: var(--ink);
  }
  .product-name, .product-sub {
    font-family: "Smokum", serif;
    fill: var(--ink);
  }
  .spec {
    font-family: "Arimo", sans-serif;
    fill: var(--ink);
    font-size: 18px;
  }
</style>
</head>
<body>
<main class="canvas">

  <svg class="label label--gin" viewBox="0 0 528 528" aria-label="VORN London Dry Gin label">
    <defs>
      <linearGradient id="gin-foliage" x1="0" y1="0" x2="1" y2="1">
        <stop offset="0" stop-color="var(--gin-mid)"/>
        <stop offset="0.45" stop-color="var(--gin-deep)"/>
        <stop offset="0.75" stop-color="var(--gin-bright)"/>
        <stop offset="1" stop-color="var(--gin-deep)"/>
      </linearGradient>
    </defs>
    <polygon class="label-field" points="264,0 528,264 264,528 0,264" fill="url(#gin-foliage)" role="img" aria-label="Dark teal photograph of tropical leaves over wood planks"/>
    <polygon class="frame-outer" points="264,21 507,264 264,507 21,264" fill="none" stroke="var(--ink)" stroke-width="4"/>
    <polygon class="frame-inner" points="264,32 496,264 264,496 32,264" fill="none" stroke="var(--gin-line)" stroke-width="2.5"/>

    <rect class="brand-square" x="228" y="95" width="75" height="78" rx="8" fill="var(--ink)"/>
    <text class="brand-name" x="264" y="217" text-anchor="middle" font-size="52" textLength="138" lengthAdjust="spacingAndGlyphs">VORN</text>

    <text class="product-name" x="264" y="303" text-anchor="middle" font-size="66" textLength="342" lengthAdjust="spacingAndGlyphs">LONDON DRY</text>
    <polygon class="rule" points="123,332 223,329 221,332 223,335" fill="var(--ink)"/>
    <text class="product-sub" x="264" y="349" text-anchor="middle" font-size="42" textLength="58" lengthAdjust="spacingAndGlyphs">GIN</text>
    <polygon class="rule" points="403,332 305,329 307,332 305,335" fill="var(--ink)"/>

    <text class="spec" x="264" y="405" text-anchor="middle">700 ml</text>
    <line x1="223" y1="411" x2="305" y2="411" stroke="var(--ink)" stroke-width="1"/>
    <text class="spec" x="264" y="429" text-anchor="middle">40% Vol</text>
  </svg>

  <svg class="label label--vodka" viewBox="0 0 528 528" aria-label="VORN Premium Vodka label">
    <defs>
      <linearGradient id="vodka-foliage" x1="0" y1="0" x2="1" y2="1">
        <stop offset="0" stop-color="var(--vodka-mid)"/>
        <stop offset="0.45" stop-color="var(--vodka-deep)"/>
        <stop offset="0.75" stop-color="var(--vodka-bright)"/>
        <stop offset="1" stop-color="var(--vodka-deep)"/>
      </linearGradient>
    </defs>
    <polygon class="label-field" points="264,0 528,264 264,528 0,264" fill="url(#vodka-foliage)" role="img" aria-label="Dark green photograph of tropical leaves over wood planks"/>
    <polygon class="frame-outer" points="264,21 507,264 264,507 21,264" fill="none" stroke="var(--ink)" stroke-width="4"/>
    <polygon class="frame-inner" points="264,32 496,264 264,496 32,264" fill="none" stroke="var(--vodka-line)" stroke-width="2.5"/>

    <rect class="brand-square" x="228" y="95" width="75" height="78" rx="8" fill="var(--ink)"/>
    <text class="brand-name" x="264" y="217" text-anchor="middle" font-size="52" textLength="138" lengthAdjust="spacingAndGlyphs">VORN</text>

    <text class="product-name" x="264" y="303" text-anchor="middle" font-size="66" textLength="171" lengthAdjust="spacingAndGlyphs">VODKA</text>
    <polygon class="rule" points="124,334 179,331 177,334 179,337" fill="var(--ink)"/>
    <text class="product-sub" x="264" y="349" text-anchor="middle" font-size="38" textLength="160" lengthAdjust="spacingAndGlyphs">PREMIUM</text>
    <polygon class="rule" points="404,334 350,331 352,334 350,337" fill="var(--ink)"/>

    <text class="spec" x="264" y="405" text-anchor="middle">700 ml</text>
    <line x1="223" y1="411" x2="305" y2="411" stroke="var(--ink)" stroke-width="1"/>
    <text class="spec" x="264" y="429" text-anchor="middle">40% Vol</text>
  </svg>

</main>
</body>
</html>
```